inventory management app design

I am looking for design ideas for an inventory management app that will work across platforms.

There are 4 components - we will need icons here and artist impressions. Details below.
- Dashboard
- Inventory and Stock Take
- Reports
- Settings

In Detail, we will need to demonstrate:
- Dashboard
Inventory Overview and Dashboard

- Inventory: table/list view that shows product image + Stock on Hand
1) View all available Inventory and what's on hand
2) Allow to run new Inventory Stock Take
2.1) list of all inventory items
2.2) tapping on inventory goes to detailed overview
2.3) finalise stock take
3) Manage recepies

- Reports
1) Wastage report

- Settings
no detailed design needed. Just please have an icon designed on the first page that indicates settings

Target Market(s)

Bars & restaurants

Industry/Entity Type

Consulting

Font styles to use
Sans Serif

Colors
0255a3
9bcb3b
ec1f27
aaaaaa
000000

Requirements
Must have
• a clean professional look
• Clearly show the different styles of pages
Nice to have
• would be good if it looked a bit like a finance app
• also good to show what the content would look like on mobile, tablet & desktop

```html
<!DOCTYPE html>
<html lang="en">
<head>
<meta charset="utf-8">
<title>Stock Dashboard</title>
<link href="https://fonts.googleapis.com/css2?family=Roboto:wght@400;500;700&display=swap" rel="stylesheet">
<style>
  :root{
    --brand-blue:#0255a3;
    --accent-yellow:#f7c300;
    --ring-fill:#d7e9fb;
    --ring-track:#9fc8f2;
    --page-bg:#f4f5f8;
    --page-shape:#e9ebf1;
    --text-dark:#111111;
    --text-muted:#8a8a8a;
    --line:#dddddd;
    --icon-grey:#9a9a9a;
    --white:#ffffff;
    --search-placeholder:#b8c9e4;
  }
  *{box-sizing:border-box;margin:0;padding:0}
  html,body{width:1200px;height:1000px;overflow:hidden}
  body{font-family:"Roboto",Arial,sans-serif;background:var(--page-bg);position:relative;color:var(--text-dark)}
  .backdrop{position:absolute;inset:0}
  .app-window{position:absolute;left:38px;top:184px;width:1124px;height:632px;background:var(--white);border-radius:20px;overflow:hidden;box-shadow:0 10px 40px rgba(40,50,80,.10)}
  .sidebar{position:absolute;left:0;top:0;width:57px;height:100%;background:var(--white);border-right:1px solid #eeeeee}
  .brand-name{position:absolute;left:0;top:16px;width:57px;text-align:center;font-weight:700;font-size:11px;color:var(--text-dark)}
  .nav-icon{position:absolute;left:18px;width:22px;height:22px}
  .nav-active-bar{position:absolute;left:54px;top:238px;width:3px;height:40px;background:var(--accent-yellow)}
  .header{position:absolute;left:57px;top:0;right:0;height:191px;background:var(--brand-blue)}
  .header-label{position:absolute;left:56px;top:34px;color:var(--white);font-size:13px}
  .welcome-title{position:absolute;left:56px;top:76px;color:var(--accent-yellow);font-size:33px;line-height:44px;font-weight:400}
  .add-stock{position:absolute;right:54px;top:18px;display:flex;align-items:center;gap:12px;color:var(--white);font-size:14px}
  .add-button{width:48px;height:48px;border-radius:50%;background:var(--accent-yellow);display:flex;align-items:center;justify-content:center}
  .search-field{position:absolute;left:535px;top:104px;width:478px;height:53px;border-bottom:1px solid rgba(255,255,255,.8)}
  .search-placeholder{position:absolute;left:2px;top:6px;font-size:26px;color:var(--search-placeholder)}
  .search-icon{position:absolute;right:0;top:8px}
  .section-title{position:absolute;font-size:14px;font-weight:500;color:var(--text-dark)}
  .section-hint{position:absolute;font-size:8px;color:var(--text-muted)}
  .product-card{position:absolute;top:254px;width:214px;height:60px;background:var(--white);border:1px solid #eeeeee;box-shadow:0 1px 4px rgba(0,0,0,.06);border-radius:3px}
  .product-image{position:absolute;left:15px;top:10px;width:14px;height:40px;border-radius:3px}
  .product-name{position:absolute;left:44px;top:16px;font-size:13px;font-weight:500;white-space:nowrap}
  .product-meta{position:absolute;left:44px;top:33px;font-size:10px;color:var(--text-muted)}
  .category-ring{position:absolute;width:70px;text-align:center}
  .category-ring svg{display:block}
  .category-label{font-size:11px;font-weight:500;margin-top:5px}
  .wastage-filter{position:absolute;left:810px;top:349px;width:260px;height:33px;border:1px solid #cfcfcf;border-radius:3px;display:flex;font-size:9px}
  .filter-cell{position:relative;border-right:1px solid #cfcfcf;height:100%}
  .filter-cell:last-child{border-right:none}
  .filter-category{width:86px;padding:11px 0 0 6px}
  .filter-date{width:87px;padding:5px 0 0 6px}
  .filter-date small{display:block;font-size:6px;color:var(--brand-blue);font-weight:700;line-height:7px}
  .filter-date span{font-size:10px}
  .filter-icon{position:absolute;right:6px;top:11px}
  .wastage-chart{position:absolute;left:590px;top:410px}
  .chart-tooltip{position:absolute;left:859px;top:428px;width:88px;height:51px;background:var(--white);border-radius:4px;box-shadow:0 2px 8px rgba(0,0,0,.18);text-align:center}
  .chart-tooltip small{display:block;font-size:7px;color:#555;margin-top:9px}
  .chart-tooltip strong{display:block;font-size:17px;font-weight:500;margin-top:6px}
  .total-wastage{position:absolute;left:882px;top:578px;font-size:10px;line-height:13px}
  .total-amount{position:absolute;right:54px;top:576px;font-size:20px;font-weight:700}
</style>
</head>
<body>
<svg class="backdrop" width="1200" height="1000" aria-hidden="true">
  <polygon points="0,0 480,150 1200,150 1200,0" fill="#f7f8fa"/>
  <polygon points="0,20 480,150 520,230 0,230" fill="var(--page-shape)"/>
  <polygon points="760,760 1200,700 1200,1000 880,1000" fill="var(--page-shape)"/>
  <polygon points="0,820 520,1000 0,1000" fill="#eef0f4"/>
</svg>

<main class="app-window">
  <aside class="sidebar">
    <div class="brand-name">Vonkel</div>
    <svg class="nav-icon" style="top:247px" viewBox="0 0 22 22"><path d="M3 11 L11 3 L19 11 V19 H13 V14 H9 V19 H3 Z" fill="var(--accent-yellow)"/></svg>
    <div class="nav-active-bar"></div>
    <svg class="nav-icon" style="top:286px" viewBox="0 0 22 22"><path d="M2 5 H9 L11 7 H20 V18 H2 Z" fill="none" stroke="var(--icon-grey)" stroke-width="1.5" stroke-linejoin="round"/></svg>
    <svg class="nav-icon" style="top:325px" viewBox="0 0 22 22"><circle cx="11" cy="11" r="8" fill="none" stroke="var(--icon-grey)" stroke-width="1.5"/><path d="M11 11 V3 M11 11 L17 15" stroke="var(--icon-grey)" stroke-width="1.5"/></svg>
    <svg class="nav-icon" style="top:365px" viewBox="0 0 22 22"><g stroke="var(--icon-grey)" stroke-width="2.4" stroke-linecap="round"><path d="M11 2.5 V4.5 M11 17.5 V19.5 M2.5 11 H4.5 M17.5 11 H19.5 M5 5 L6.4 6.4 M15.6 15.6 L17 17 M5 17 L6.4 15.6 M15.6 6.4 L17 5"/></g><circle cx="11" cy="11" r="6" fill="none" stroke="var(--icon-grey)" stroke-width="1.5"/><circle cx="11" cy="11" r="2.5" fill="none" stroke="var(--icon-grey)" stroke-width="1.3"/></svg>
    <svg class="nav-icon" style="top:602px" viewBox="0 0 22 22"><path d="M7 5 L3 9 L7 13 M3 9 H14 A5 5 0 0 1 14 19 H9" fill="none" stroke="var(--icon-grey)" stroke-width="1.5" stroke-linecap="round" stroke-linejoin="round"/></svg>
  </aside>

  <header class="header">
    <div class="header-label">Overview</div>
    <h1 class="welcome-title">Welcome to your<br>Dashboard, Jonas!</h1>
    <div class="add-stock">Add new stock item
      <span class="add-button"><svg width="22" height="22" viewBox="0 0 22 22"><path d="M11 3 V19 M3 11 H19" stroke="var(--white)" stroke-width="2.2" stroke-linecap="round"/></svg></span>
    </div>
    <div class="search-field">
      <span class="search-placeholder">Search</span>
      <svg class="search-icon" width="30" height="30" viewBox="0 0 30 30"><circle cx="12" cy="12" r="10" fill="none" stroke="var(--white)" stroke-width="1.5"/><path d="M19.5 19.5 L28 28" stroke="var(--white)" stroke-width="1.5" stroke-linecap="round"/></svg>
    </div>
  </header>

  <h2 class="section-title" style="left:113px;top:211px">Stock taking overview</h2>
  <p class="section-hint" style="left:114px;top:230px">Tap or click to get detailed overview</p>

  <div class="product-card" style="left:114px">
    <div class="product-image" role="img" aria-label="Vodka bottle product photo" style="background:linear-gradient(#dfe6ef,#aab8cc)"></div>
    <div class="product-name">Northfield Vodka Classic</div><div class="product-meta">700 ml • Vodka</div>
  </div>
  <div class="product-card" style="left:353px">
    <div class="product-image" role="img" aria-label="Gin bottle product photo" style="background:linear-gradient(#d9eec4,#8fc46a)"></div>
    <div class="product-name">Harbour Gin 10</div><div class="product-meta">700 ml • Gin</div>
  </div>
  <div class="product-card" style="left:593px">
    <div class="product-image" role="img" aria-label="Wine bottle product photo" style="background:linear-gradient(#5a3a3a,#1c1414)"></div>
    <div class="product-name">Velmora Shiraz Rosé</div><div class="product-meta">700 ml • Wine</div>
  </div>
  <div class="product-card" style="left:832px">
    <div class="product-image" role="img" aria-label="Beer bottle product photo" style="background:linear-gradient(#3f7a3a,#c8a040 60%,#a3362a)"></div>
    <div class="product-name">Rio Claro Lager</div><div class="product-meta">330 ml • Beer</div>
  </div>

  <h2 class="section-title" style="left:113px;top:350px">Stock on Hand Category</h2>
  <p class="section-hint" style="left:114px;top:370px">Tap or click to get detailed category.</p>

  <div class="category-ring" style="left:112px;top:393px"><svg width="70" height="70" viewBox="0 0 70 70"><circle cx="35" cy="35" r="32" fill="none" stroke="var(--ring-track)" stroke-width="1.2"/><circle cx="35" cy="35" r="32" fill="none" stroke="var(--brand-blue)" stroke-width="3" pathLength="100" stroke-dasharray="10 90" transform="rotate(-90 35 35)"/><circle cx="35" cy="35" r="25" fill="var(--ring-fill)"/><text x="35" y="40" text-anchor="middle" font-size="14">10%</text></svg><div class="category-label">Wine</div></div>
  <div class="category-ring" style="left:232px;top:393px"><svg width="70" height="70" viewBox="0 0 70 70"><circle cx="35" cy="35" r="32" fill="none" stroke="var(--ring-track)" stroke-width="1.2"/><circle cx="35" cy="35" r="32" fill="none" stroke="var(--brand-blue)" stroke-width="3" pathLength="100" stroke-dasharray="15 85" transform="rotate(-90 35 35)"/><circle cx="35" cy="35" r="25" fill="var(--ring-fill)"/><text x="35" y="40" text-anchor="middle" font-size="14">15%</text></svg><div class="category-label">Beer</div></div>
  <div class="category-ring" style="left:350px;top:393px"><svg width="70" height="70" viewBox="0 0 70 70"><circle cx="35" cy="35" r="32" fill="none" stroke="var(--ring-track)" stroke-width="1.2"/><circle cx="35" cy="35" r="32" fill="none" stroke="var(--brand-blue)" stroke-width="3" pathLength="100" stroke-dasharray="25 75" transform="rotate(-90 35 35)"/><circle cx="35" cy="35" r="25" fill="var(--ring-fill)"/><text x="35" y="40" text-anchor="middle" font-size="14">25%</text></svg><div class="category-label">Vodka</div></div>
  <div class="category-ring" style="left:470px;top:393px"><svg width="70" height="70" viewBox="0 0 70 70"><circle cx="35" cy="35" r="32" fill="none" stroke="var(--ring-track)" stroke-width="1.2"/><circle cx="35" cy="35" r="32" fill="none" stroke="var(--brand-blue)" stroke-width="3" pathLength="100" stroke-dasharray="15 85" transform="rotate(-90 35 35)"/><circle cx="35" cy="35" r="25" fill="var(--ring-fill)"/><text x="35" y="40" text-anchor="middle" font-size="14">15%</text></svg><div class="category-label">Gin</div></div>
  <div class="category-ring" style="left:112px;top:507px"><svg width="70" height="70" viewBox="0 0 70 70"><circle cx="35" cy="35" r="32" fill="none" stroke="var(--ring-track)" stroke-width="1.2"/><circle cx="35" cy="35" r="32" fill="none" stroke="var(--brand-blue)" stroke-width="3" pathLength="100" stroke-dasharray="10 90" transform="rotate(-90 35 35)"/><circle cx="35" cy="35" r="25" fill="var(--ring-fill)"/><text x="35" y="40" text-anchor="middle" font-size="14">10%</text></svg><div class="category-label">Whisky</div></div>
  <div class="category-ring" style="left:232px;top:507px"><svg width="70" height="70" viewBox="0 0 70 70"><circle cx="35" cy="35" r="32" fill="none" stroke="var(--ring-track)" stroke-width="1.2"/><circle cx="35" cy="35" r="32" fill="none" stroke="var(--brand-blue)" stroke-width="3" pathLength="100" stroke-dasharray="10 90" transform="rotate(-90 35 35)"/><circle cx="35" cy="35" r="25" fill="var(--ring-fill)"/><text x="35" y="40" text-anchor="middle" font-size="14">10%</text></svg><div class="category-label">Liqueur</div></div>
  <div class="category-ring" style="left:350px;top:507px"><svg width="70" height="70" viewBox="0 0 70 70"><circle cx="35" cy="35" r="32" fill="none" stroke="var(--ring-track)" stroke-width="1.2"/><circle cx="35" cy="35" r="32" fill="none" stroke="var(--brand-blue)" stroke-width="3" pathLength="100" stroke-dasharray="15 85" transform="rotate(-90 35 35)"/><circle cx="35" cy="35" r="25" fill="var(--ring-fill)"/><text x="35" y="40" text-anchor="middle" font-size="14">15%</text></svg><div class="category-label">Softdrinks</div></div>
  <div class="category-ring" style="left:470px;top:507px"><svg width="70" height="70" viewBox="0 0 70 70"><circle cx="35" cy="35" r="32" fill="none" stroke="var(--ring-track)" stroke-width="1.2"/><circle cx="35" cy="35" r="32" fill="none" stroke="var(--brand-blue)" stroke-width="3" pathLength="100" stroke-dasharray="15 85" transform="rotate(-90 35 35)"/><circle cx="35" cy="35" r="25" fill="var(--ring-fill)"/><text x="35" y="40" text-anchor="middle" font-size="14">15%</text></svg><div class="category-label">Other</div></div>

  <h2 class="section-title" style="left:592px;top:350px">Wastage</h2>
  <p class="section-hint" style="left:593px;top:370px">Tap or click to get detailed reports.</p>

  <div class="wastage-filter">
    <div class="filter-cell filter-category">All Category
      <svg class="filter-icon" width="11" height="9" viewBox="0 0 11 9"><path d="M0 1 H11 M2 4.5 H9 M4 8 H7" stroke="var(--brand-blue)" stroke-width="1.3"/></svg></div>
    <div class="filter-cell filter-date"><small>Start</small><span>01/02/18</span>
      <svg class="filter-icon" style="top:15px" width="10" height="10" viewBox="0 0 10 10"><rect x="0.5" y="1.5" width="9" height="8" fill="none" stroke="var(--brand-blue)"/><rect x="0.5" y="1.5" width="9" height="2.5" fill="var(--brand-blue)"/><rect x="5" y="5.5" width="2.5" height="2.5" fill="var(--brand-blue)"/></svg></div>
    <div class="filter-cell filter-date"><small>End</small><span>30/12/18</span>
      <svg class="filter-icon" style="top:15px" width="10" height="10" viewBox="0 0 10 10"><rect x="0.5" y="1.5" width="9" height="8" fill="none" stroke="var(--brand-blue)"/><rect x="0.5" y="1.5" width="9" height="2.5" fill="var(--brand-blue)"/><rect x="5" y="5.5" width="2.5" height="2.5" fill="var(--brand-blue)"/></svg></div>
  </div>

  <svg class="wastage-chart" width="490" height="160" viewBox="0 0 490 160" font-family="Roboto, Arial, sans-serif">
    <g font-size="8" font-weight="700" fill="var(--text-dark)">
      <text x="2" y="8">$ 1000</text><text x="2" y="50">$ 500</text><text x="2" y="93">$ 100</text><text x="2" y="135">$ 0</text>
    </g>
    <g stroke="var(--line)" stroke-width="1">
      <line x1="30" y1="5" x2="480" y2="5"/><line x1="30" y1="47" x2="480" y2="47"/><line x1="30" y1="90" x2="480" y2="90"/>
    </g>
    <g fill="var(--brand-blue)">
      <rect x="31" y="69" width="29" height="62"/><rect x="69" y="55" width="29" height="76"/><rect x="107" y="52" width="30" height="79"/>
      <rect x="145" y="60" width="30" height="71"/><rect x="183" y="50" width="30" height="81"/><rect x="222" y="40" width="29" height="91"/>
      <rect x="260" y="37" width="29" height="94"/><rect x="298" y="62" width="29" height="69"/><rect x="336" y="35" width="29" height="96"/>
      <rect x="374" y="33" width="30" height="98"/><rect x="413" y="21" width="29" height="110"/><rect x="451" y="21" width="29" height="110"/>
    </g>
    <g font-size="8" font-weight="700" text-anchor="middle" fill="var(--text-dark)">
      <text x="45" y="144">Jan</text><text x="83" y="144">Feb</text><text x="122" y="144">Mar</text><text x="160" y="144">Apr</text>
      <text x="198" y="144">May</text><text x="236" y="144">Jun</text><text x="274" y="144">Jul</text><text x="312" y="144">Aug</text>
      <text x="350" y="144">Sep</text><text x="389" y="144">Oct</text><text x="427" y="144">Nov</text><text x="465" y="144">Dec</text>
    </g>
    <line x1="30" y1="158" x2="480" y2="158" stroke="var(--line)"/>
    <path d="M312 96 v-8 a1.5 1.5 0 0 1 3 0 v7 l1-0.5 a1.5 1.5 0 0 1 3 0 l1 0 a1.5 1.5 0 0 1 3 0.5 v6 c0 3-2 5-5 5 h-2 c-2 0-3-1-4-3 l-3-4 a1.5 1.5 0 0 1 2.5-1.5 z" fill="var(--white)" stroke="var(--text-dark)" stroke-width="0.9"/>
  </svg>

  <div class="chart-tooltip"><small>1 - 31 August 2018</small><strong>$ 500</strong></div>

  <div class="total-wastage">Total wastage<br>Last year</div>
  <div class="total-amount">$&nbsp; 1.234.456</div>
</main>
</body>
</html>
```